Website - TSCR

Having reviewed the designs received so far, no one design is meeting the client’s needs. The client has identified desirable elements from the designs submitted, which we want to see brought together.
Header
It is important that the logo is given space – ie is not overlayed on an image, nor with a short fade into an image. A gradual fade into the header image is acceptable.
Background
While an image background is acceptable, this should only be visible on the left and right borders, it should not be used underneath the main content area.
Main menu
The main menu should be a cohesive bar across the page – not separate buttons. Buttons that are connected together within a bar are acceptable. Menu items should be separated using a pipe ( | ), or by being framed (as long as the framing sits within a bar). Menu item should change colour to indicate the page you are on.
Left Hand Boxes
There should be consistency in colouring through these. It is acceptable to use one colour for the heading , and another for the content area. It is not acceptable for each box to have a different scheme. This applies to the right hand feature boxes as well.
Colouring
We want to keep this simple. Please use colours from the logo, feel free to add complimentary colours but keep the palette limited. If shading is used with any of the colours be careful to not move it too far from the original colour. The yellow does not look good with too much of a grey shade.
Feature Boxes
The two feature boxes on the home page (Browse Homes and Local Knowledge) need to stand out. An option is to ensure that the associated link button uses one of the brighter colours in the palette.
_____________________________________________________
Note: I have attached the newly design logo to the brief. It is important that colours from the logo are used on the design. Blue denotes water and the yellow denotes sand and sun.
I'd like to see the feel of the logo reflected in the site.
______________________________________________
Tui Shore and Coastal Retreats is rebuilding its website – www.tuishoreandcoastalretreats.co.nz.
We require the design of two pages:
• Home
• House detail page (pgs 3-5 of the attachment).
We have specified a layout for the site (attached).
The contextual information below provides the feeling the site needs to convey.
If further information is required please contact us.
CONTEXT/BACKGROUND
Tui Shore and Coastal Retreats (TSCR) has been in business now for over 11 years and is due for a facelift. We have about 40 – 60 houses available during the peak summer period – about 50% are permanent holiday homes, the balance are local family homes being rented out while they are away on holiday.
We are currently located in Ohope Beach – but with the national name have the ability and goal to expand into other areas of New Zealand – so any logo etc has to have the ability to represent other holiday destinations within NZ. Bear in mind that our primary location is Ohope at the moment.
Our key market is families going on holiday – looking for a holiday home to book (currently an Ohope Beach holiday)
Secondary market is couples or mature groups looking at having some R&R or business groups having some team building/ management meetings away from the busy office surroundings.
We manage ALL the properties so are a great source of information on what holiday home is best suited to each family and “things to do” in the area – i.e. other activities.
Our main focus is to be the best “holiday home” - accommodation provider in whatever location TSCR is representing. We want to be seen as having a good supply of great homes, providing a great service as well as being a good source of local knowledge.
We want to be seen as PROFESSIONALS in the holiday rental business (from occupants and owners).
TRUST – we want people to be able to trust us by listing their property with us (owners) and confidently booking accommodation through us (occupants).
TAGLINE SUGGESTIONS
Key motif – “TSCR, your door to a fine escape!” The “key”, of course is a double play on the house key you get. But it is also extendible to other aspect of the experience we offer. For example the phrase: “getting the key to the city” is applicable to us – we give them the key to Ohope…(or whatever location we are marketing in the future). Potentially we may consider promotional merchandise around this, eg promo key rings etc.
Some key words/phrases that our business represents are:
• ‘Our place is your place’
• Connect – connecting families to holiday homes and the area – at the moment only Ohope.
• Local – local people looking after your needs – “our place is your place – so make yourself at home!”
• Link – we are the link to a real kiwi holiday experience.
• Holiday - R&R – rest and recreation
More specific to Ohope:
• Safe Natural playground – beach, bush, fishing, outdoor activities – creating real family memories.
Website:
• Need to focus on the Local and Personal property management factors in website to differentiate us from other nationwide listing sites – contact us and we can help you find the right accommodation and save you time
• Play on the HOLIDAYMAKER experience more, including giving prominence to visitor deals, become a local etc, differentiating us from other local holiday home rental businesses.
• Real – real people, real places, real experiences.
• User friendly, informative, professional with a personal touch/feel, to encourage the holiday feeling.
Reason: We had put this project on hold pending the design of a new logo.
Having reviewed the designs received so far, no one design is meetingthe client’s needs. The client has identified desirable elements from thedesigns submitted, which we want to see brought together.
Header
It is important that the logo is given space – ie is not overlayed on animage, nor with a short fade into an image. A gradual fade into the headerimage is acceptable.
Background
While an image background is acceptable, this should only be visible onthe left and right borders, it should not be used underneath the main contentarea.
Main menu
The main menu should be a cohesive bar across the page – not separatebuttons. Buttons that are connected together within a bar are acceptable.Menu items should be separated using a pipe ( | ), or by being framed (as longas the framing sits within a bar). Menu item should change colour to indicatethe page you are on.
Left Hand Boxes
There should be consistency in colouring through these. It isacceptable to use one colour for the heading , and another for the contentarea. It is not acceptable for each box to have a different scheme. Thisapplies to the right hand feature boxes as well.
Colouring
We want to keep this simple. Please use colours from the logo,feel free to add complimentary colours but keep the palette limited. Ifshading is used with any of the colours be careful to not move it too far fromthe original colour. The yellow does not look good with too much of agrey shade.
Feature Boxes
The two feature boxes on the home page (Browse Homes and LocalKnowledge) need to stand out. An option is to ensure that the associated linkbutton uses one of the brighter colours in the palette.

```html
<!DOCTYPE html>
<html lang="en">
<head>
<meta charset="utf-8">
<title>Tui Shore &amp; Coastal Retreats – Home</title>
<link href="https://fonts.googleapis.com/css2?family=Arimo:wght@400;700&family=Cuprum:wght@400;700&display=swap" rel="stylesheet">
<style>
:root{
  --blue:#0a6fc6;
  --blue-light:#1e8fe6;
  --blue-dark:#0760ae;
  --sky:#2f9be3;
  --yellow:#ffc20e;
  --yellow-light:#ffdf3a;
  --cream:#fffdf3;
  --ink:#333333;
  --grey-bg:#6b6b6b;
  --dark-head:#3a3a3a;
  --panel-blue:#e7f3fc;
  --red:#e8101c;
  --white:#ffffff;
}
*{box-sizing:border-box;margin:0;padding:0}
html,body{width:1164px;height:1200px;overflow:hidden}
body{position:relative;background:var(--grey-bg);font-family:"Arimo",Arial,sans-serif;color:var(--ink)}
.side-scenery{position:absolute;top:0;height:308px;background:linear-gradient(180deg,#d7e7ee 0%,#3f7f3a 30%,#2d6a2d 60%,#bcd7e2 78%,#6fa3bd 100%)}
.side-scenery.left{left:0;width:80px}
.side-scenery.right{right:0;width:114px}
.page{position:absolute;left:80px;top:0;width:970px;height:1122px;background:var(--white)}
.header{position:absolute;left:0;top:0;width:970px;height:267px}
.logo-panel{position:absolute;left:0;top:0;width:262px;height:267px;background:linear-gradient(180deg,#f4f9fd,#e9f3fb);border-right:1px solid #c9dcea;display:flex;align-items:center;justify-content:center;gap:10px;padding:0 18px}
.logo-dot{width:22px;height:22px;border-radius:50%;background:var(--yellow);flex:none}
.logo-name{font-family:"Cuprum",sans-serif;font-size:25px;line-height:1.1;color:#3b3b3b;font-weight:400}
.hero{position:absolute;left:262px;top:0;width:708px;height:267px;background:linear-gradient(100deg,#3fa3e6 0%,#6cbcec 35%,#e6eef2 55%,#5a8a72 72%,#2c6d7c 85%,#1c5f86 100%)}
.hero-title{position:absolute;top:24px;color:var(--white);font-family:"Arimo",sans-serif;font-weight:700;font-size:28px;line-height:34px;text-shadow:0 1px 2px rgba(0,0,0,.25)}
.hero-title .l1{display:block;margin-left:48px}
.hero-title .l2{display:block;margin-left:180px}
.main-nav{position:absolute;left:0;top:267px;width:970px;height:41px;background:linear-gradient(180deg,var(--blue-light),var(--blue-dark));display:flex;align-items:stretch}
.nav-item{font-family:"Cuprum",sans-serif;font-size:19px;color:var(--white);display:flex;align-items:center;padding:0 12px;border-right:1px solid rgba(255,255,255,.35)}
.nav-item.active{background:linear-gradient(180deg,var(--yellow-light),var(--yellow));color:#2b2b2b;margin-top:-9px;border-radius:6px 6px 0 0;padding-top:9px;border-right:0}
.nav-item.home{padding:0 12px 0 22px}
.sidebar{position:absolute;left:10px;top:319px;width:262px}
.box{position:absolute;left:0;width:262px;border-radius:4px;overflow:hidden}
.box-head{height:37px;font-family:"Cuprum",sans-serif;font-weight:700;font-size:24px;padding:2px 9px;line-height:36px}
.quick{top:0;height:248px;border:1px solid var(--yellow);background:var(--cream)}
.quick .box-head{background:linear-gradient(180deg,var(--yellow-light),var(--yellow));color:#2b2b2b}
.field-label{position:absolute;left:9px;font-size:13px;color:#222}
.select{position:absolute;height:28px;border:1px solid #bbb;border-radius:3px;background:linear-gradient(180deg,#fff,#e8e8e8)}
.select::after{content:"";position:absolute;right:4px;top:6px;width:14px;height:14px;background:#ddd;border:1px solid #999}
.select i{position:absolute;right:8px;top:11px;width:0;height:0;border-left:4px solid transparent;border-right:4px solid transparent;border-top:6px solid #222;z-index:1}
.text-input{position:absolute;height:28px;border:1px solid #bbb;border-radius:3px;background:linear-gradient(180deg,#fff,#eaeaea);font-size:11px;color:#777;padding:7px 7px}
.go-btn{position:absolute;height:28px;border-radius:4px;background:linear-gradient(180deg,#666,#2f2f2f);color:var(--white);font-weight:700;font-size:15px;display:flex;align-items:center;justify-content:center}
.link{color:var(--blue);font-size:12px}
.touch{top:269px;height:216px;border:1px solid var(--blue)}
.touch .box-head,.deals .box-head{background:linear-gradient(180deg,var(--blue-light),var(--blue-dark));color:var(--white)}
.touch-intro{text-align:center;font-size:15px;line-height:22px;color:#444;margin-top:5px}
.deals{top:509px;height:216px;border:1px solid #aaa;background:linear-gradient(180deg,#fff,#f0f0f0)}
.deal-photo{position:absolute;left:6px;top:44px;width:118px;height:128px;background:linear-gradient(180deg,#bfe3f5,#e8f4fb 60%,#cfe5ee)}
.deal-text{position:absolute;left:134px;top:40px;width:124px;font-size:13.5px;line-height:22px;color:#333}
.share{position:absolute;left:0;top:739px;width:262px;height:52px;border:1px solid #b8cfe0;background:var(--panel-blue);display:flex;align-items:center;padding-left:4px;gap:20px;font-size:14px}
.share-tile{width:36px;height:36px;border-radius:3px;background:var(--sky)}
.content{position:absolute;left:293px;top:308px;width:665px}
.welcome{position:absolute;left:0;top:16px;font-family:"Cuprum",sans-serif;font-size:23px;color:var(--blue)}
.copy{position:absolute;font-size:12.4px;line-height:16.8px;color:#333;text-align:justify}
.shortlist{position:absolute;left:516px;top:17px;width:139px;height:85px;border-radius:4px;background:linear-gradient(180deg,var(--yellow-light),var(--yellow) 60%,#f5a800);border:1px solid #e19b00;text-align:center;color:var(--white);font-weight:700;font-size:27px;line-height:30px;padding-top:10px;text-shadow:0 1px 3px rgba(0,0,0,.45)}
.help{position:absolute;left:516px;top:112px;width:139px;height:205px;border-radius:4px;background:linear-gradient(180deg,#eaf5fd,#fff);border:1px solid #cfe2f0;text-align:center;box-shadow:0 1px 3px rgba(0,0,0,.15)}
.help h3{font-size:26px;color:var(--blue);margin-top:8px}
.help p{font-weight:700;font-size:14.5px;line-height:21px;color:#444;margin-top:4px;letter-spacing:.3px}
.help .phone{color:var(--red);font-size:15px;margin-top:6px;letter-spacing:0}
.cta{position:absolute;left:0;top:478px;width:670px;text-align:center;font-weight:700;font-size:23px;line-height:33px;color:#333}
.cta .accent{color:var(--blue)}
.feature{position:absolute;top:563px;height:239px;border-radius:4px;overflow:hidden;box-shadow:0 2px 4px rgba(0,0,0,.3)}
.feature .photo{height:198px}
.feature .label{height:41px;display:flex;align-items:center;justify-content:center;color:var(--white);font-weight:700;font-size:17px}
.feature.homes{left:0;width:331px;border:1px solid var(--blue)}
.feature.homes .photo{background:linear-gradient(180deg,#3b6c9a,#9a7a4a 45%,#c88a3a 70%,#2a6f8c)}
.feature.homes .label{background:linear-gradient(180deg,#2aa4ff,#1188ee)}
.feature.local{left:351px;width:304px;border:1px solid var(--yellow)}
.feature.local .photo{background:linear-gradient(180deg,#6fb4e8,#4c8a3b 35%,#44b4d8 65%,#2fa6c8)}
.feature.local .label{background:linear-gradient(180deg,var(--yellow-light),var(--yellow))}
.footer{position:absolute;left:0;top:1122px;width:1164px;height:78px;background:var(--blue)}
.footer-links{position:absolute;top:17px;left:372px;display:flex;gap:16px;font-size:14px;color:var(--white)}
</style>
</head>
<body>
<div class="side-scenery left" role="img" aria-label="Coastal island scenery background"></div>
<div class="side-scenery right" role="img" aria-label="Coastal island scenery background"></div>

<div class="page">
  <header class="header">
    <div class="logo-panel">
      <span class="logo-dot"></span>
      <span class="logo-name">Tui Shore &amp; Coastal Retreats</span>
    </div>
    <div class="hero" role="img" aria-label="Woman sunbathing on a white sand beach beside an aerial view of a green coastal bay">
      <div class="hero-title"><span class="l1">Lorem Ipsum Dlor Sit</span><span class="l2">Ipsum Dlor Sit</span></div>
    </div>
  </header>

  <nav class="main-nav">
    <span class="nav-item home">Home</span>
    <span class="nav-item">Browse Homes</span>
    <span class="nav-item">Packages</span>
    <span class="nav-item active">Local Knowledge</span>
    <span class="nav-item">About us</span>
    <span class="nav-item">Contact us</span>
    <span class="nav-item">List your Homes</span>
  </nav>

  <aside class="sidebar">
    <section class="box quick">
      <div class="box-head">Quick Search</div>
      <span class="field-label" style="top:45px">No. Of Guests Beach</span>
      <div class="select" style="left:8px;top:64px;width:246px"><i></i></div>
      <span class="field-label" style="top:104px">Nightly Rate</span>
      <div class="select" style="left:8px;top:124px;width:117px"><i></i></div>
      <span class="field-label" style="left:134px;top:131px">to</span>
      <div class="select" style="left:158px;top:124px;width:96px"><i></i></div>
      <span class="field-label" style="top:166px">Keyword</span>
      <div class="text-input" style="left:8px;top:186px;width:204px">Beach Access</div>
      <div class="go-btn" style="left:211px;top:186px;width:43px;border-radius:0 4px 4px 0">GO</div>
      <span class="link" style="position:absolute;left:9px;top:228px">Advanced Search</span>
    </section>

    <section class="box touch">
      <div class="box-head">Keep In Touch</div>
      <p class="touch-intro">Newsletter with Deals &amp;<br>Local Knowledge To Your Inbox</p>
      <span class="field-label" style="top:98px;font-size:16px;left:7px">Name</span>
      <div class="text-input" style="left:56px;top:92px;width:199px"></div>
      <span class="field-label" style="top:140px;font-size:16px;left:7px">Email</span>
      <div class="text-input" style="left:56px;top:134px;width:199px"></div>
      <div class="go-btn" style="left:7px;top:176px;width:104px;height:30px;background:linear-gradient(180deg,#4d7bc0,#2b5a9d);font-weight:400;font-size:13px">Shorebook</div>
      <div class="go-btn" style="left:201px;top:176px;width:53px;height:28px">GO</div>
    </section>

    <section class="box deals">
      <div class="box-head">Deals</div>
      <div class="deal-photo" role="img" aria-label="Couple relaxing on a sun lounger by the water"></div>
      <p class="deal-text">Lorem ipsum Lorem ipsum dolor sit&nbsp; Lorem ipsum Lorem ipsum dolor sit Lorem Lorem ipsum</p>
      <span style="position:absolute;left:17px;top:189px;font-weight:700;font-size:13px;color:var(--blue)">VIEW</span>
      <div class="go-btn" style="left:201px;top:180px;width:53px;height:29px">View</div>
    </section>

    <div class="share">
      <svg width="40" height="36" viewBox="0 0 40 36" aria-label="Email">
        <rect x="2" y="6" width="36" height="26" rx="2" fill="#f2f2f2" stroke="#777" stroke-width="1.5"/>
        <path d="M2 8 L20 22 L38 8" fill="none" stroke="#777" stroke-width="1.5"/>
      </svg>
      <span class="share-tile"></span>
      <span class="share-tile" style="background:#3b5b9a"></span>
      <span style="margin-left:4px">Share This</span>
    </div>
  </aside>

  <main class="content">
    <h1 class="welcome">Welcome to Tui Shore &amp; Coastal Retreats</h1>
    <p class="copy" style="left:0;top:55px;width:484px">Lorem ipsum onsectetuer adipiscing elit, sed diam nonummy nibh euismod tincidunt ut laoreet dolore magna aliquam erat volutpat. Ut wisi enim ad minim veniam, quis nostrud exerci tation ullamcorper suscipit lobortis nisl ut aliquip ex ea commodo consequat.</p>
    <p class="copy" style="left:0;top:139px;width:484px">Lorem ipsum onsectetuer adipiscing elit, sed diam nonummy nibh euismod tincidunt ut laoreet dolore magna aliquam erat volutpat. Ut wisi enim ad minim veniam, quis nostrud exerci tation ullamcorper suscipit lobortis nisl ut aliquip ex ea commodo consequat.</p>
    <p class="copy" style="left:0;top:223px;width:484px">Lorem ipsum onsectetuer adipiscing elit, sed diam nonummy nibh euismod tincidunt ut laoreet dolore magna aliquam erat volutpat. Ut wisi enim ad minim veniam, quis nostrud exerci tation ullamcorper suscipit lobortis nisl ut aliquip ex ea commodo consequat.</p>

    <div class="shortlist">My<br>Shortlist</div>
    <div class="help">
      <h3>Help !</h3>
      <p>Can't Find What You're Looking For?<br>Contact Us For A Personal Property Search</p>
      <p class="phone">+64-21-555-0187</p>
    </div>

    <p class="copy" style="left:0;top:333px;width:651px">Lorem ipsum onsectetuer adipiscing elit, sed diam nonummy nibh euismod tincidunt ut laoreet dolore magna aliquam erat volutpat. Ut wisi enim ad minim veniam, quis nostrud exerci tation ullamcorper suscipit lobortis nisl ut aliquip ex ea commodo consequat.</p>
    <p class="copy" style="left:0;top:409px;width:651px">Lorem ipsum onsectetuer adipiscing elit, sed diam nonummy nibh euismod tincidunt ut laoreet dolore magna aliquam erat volutpat. Ut wisi enim ad minim veniam, quis nostrud exerci tation ullamcorper suscipit lobortis nisl ut aliquip ex ea commodo consequat.</p>

    <p class="cta">Just can’t find what you’re looking for?<br><span class="accent">Contact us</span> for a personal property search.</p>

    <a class="feature homes">
      <div class="photo" role="img" aria-label="Grand holiday villa lit at dusk beside a pool"></div>
      <div class="label">Browse Homes</div>
    </a>
    <a class="feature local">
      <div class="photo" role="img" aria-label="Tropical resort pool with palm trees and thatched umbrellas"></div>
      <div class="label">Local Knowledge</div>
    </a>
  </main>
</div>

<footer class="footer">
  <nav class="footer-links">
    <span style="margin-right:4px">Terms &amp; Conditions</span>
    <span style="margin-left:-2px">Privacy Policy</span>
    <span style="margin-left:-4px">Contact Us List</span>
    <span>Your Home</span>
  </nav>
</footer>
</body>
</html>
```